BRAVEN POWERLINE SERVICES needs a vibrant design for electrical contracting work.

I require a card design for my own electrical contracting business. I will be doing a lot of domestic and commercial work, including things such as repairs, maintenance, lighting, installations and various others. LED lighting and energy efficiency will be a big part of my business. I wish not to have childish pictures such as light bulbs in the design, but rather a smart and modern looking card which incorporates my logo colours and perhaps the same lighting strike within the faded background of the card.

Target Market(s)

Residential and Commercial property owners.

Industry/Entity Type

Electrical

Contact Information for Business Card

Dalen Voskic
EC40923
Phone Number: 0417 358 942
Email: dalen@bravenpowerline.com

Font styles to use
Serif
Sans Serif

Requirements
Must have
• My Logo and associated colours.
Nice to have
• Some form of shapes splitting the card into different colours related to the colours of my logo. Electric Blue, Silver/Grey and White.
Should not have
• Childish pictures and symbols such as light bulbs.

```html
<!DOCTYPE html>
<html lang="en">
<head>
<meta charset="utf-8">
<title>Braven Powerline Services – Business Card</title>
<link rel="stylesheet" href="https://fonts.googleapis.com/css2?family=Lato:wght@400;700&display=swap">
<style>
  :root {
    --backdrop: #4a4a4c;
    --card-dark: #1c1c1d;
    --card-light: #ffffff;
    --electric-blue: #3a4fa8;
    --silver: #b9bbc0;
    --ink: #1f1f1f;
    --divider: #8a8a8a;
    --faded-blue: #cfd2ec;
  }
  html, body {
    margin: 0;
    padding: 0;
    width: 1200px;
    height: 1000px;
    overflow: hidden;
    background: var(--backdrop);
    font-family: "Lato", sans-serif;
  }
  .canvas {
    position: relative;
    width: 1200px;
    height: 1000px;
  }
  .card {
    position: absolute;
    box-shadow: 0 4px 10px rgba(0, 0, 0, 0.35);
  }

  /* Front card */
  .card-front {
    left: 198px;
    top: 152px;
    width: 550px;
    height: 338px;
    background: var(--card-dark);
  }
  .brand {
    display: flex;
    align-items: center;
    gap: 12px;
    color: var(--electric-blue);
    font-weight: 700;
    white-space: nowrap;
  }
  .card-front .brand {
    position: absolute;
    left: 0;
    right: 0;
    top: 112px;
    justify-content: center;
    font-size: 25px;
    letter-spacing: 1px;
  }
  .brand-dot {
    flex: none;
    border-radius: 50%;
    background: var(--silver);
  }
  .card-front .brand-dot { width: 34px; height: 34px; }
  .services {
    position: absolute;
    left: 0;
    right: 0;
    top: 204px;
    margin: 0;
    text-align: center;
    font-size: 14.5px;
    line-height: 23px;
    color: var(--electric-blue);
  }
  .services .sep { color: var(--divider); padding: 0 2px; }

  /* Back card */
  .card-back {
    left: 467px;
    top: 534px;
    width: 540px;
    height: 332px;
    background: var(--card-light);
    overflow: hidden;
  }
  .faded-mark {
    position: absolute;
    left: 16px;
    top: 60px;
    width: 205px;
    height: 205px;
    border-radius: 50%;
    background: var(--faded-blue);
    opacity: 0.55;
  }
  .card-back .brand {
    position: absolute;
    right: 32px;
    top: 62px;
    font-size: 13px;
    letter-spacing: 0.5px;
    gap: 8px;
  }
  .card-back .brand-dot { width: 22px; height: 22px; }
  .contact {
    position: absolute;
    left: 290px;
    width: 222px;
    top: 162px;
    text-align: center;
  }
  .contact-name {
    margin: 0;
    font-size: 20px;
    font-weight: 400;
    letter-spacing: 0.5px;
    color: var(--electric-blue);
    line-height: 24px;
  }
  .licence {
    margin: 0 0 20px;
    font-size: 13.5px;
    color: var(--ink);
    line-height: 18px;
  }
  .contact-line {
    margin: 0;
    font-size: 14px;
    line-height: 22px;
    color: var(--ink);
    white-space: nowrap;
  }
  .contact-line .label { color: var(--electric-blue); }
  .footer-band {
    position: absolute;
    left: 0;
    bottom: 0;
    width: 540px;
    height: 26px;
  }
</style>
</head>
<body>
  <main class="canvas">
    <section class="card card-front" aria-label="Business card front">
      <div class="brand">
        <span class="brand-dot" aria-hidden="true"></span>
        <span class="brand-name">BRAVEN POWERLINE SERVICES</span>
      </div>
      <p class="services">
        LED Lighting <span class="sep">|</span> Energy Efficiency <span class="sep">|</span> Repairs <span class="sep">|</span> Maintenance<br>
        Lightings <span class="sep">|</span> Installations
      </p>
    </section>

    <section class="card card-back" aria-label="Business card back">
      <div class="faded-mark" role="img" aria-label="Faded brand emblem in the background"></div>
      <div class="brand">
        <span class="brand-dot" aria-hidden="true"></span>
        <span class="brand-name">BRAVEN POWERLINE SERVICES</span>
      </div>
      <div class="contact">
        <h1 class="contact-name">DALEN VOSKIC</h1>
        <p class="licence">EC40923</p>
        <p class="contact-line"><span class="label">Phone:</span> 0417 358 942</p>
        <p class="contact-line"><span class="label">Email:</span> dalen@bravenpowerline.com</p>
      </div>
      <svg class="footer-band" viewBox="0 0 540 26" aria-hidden="true">
        <polygon points="0,0 280,0 276,26 0,26" fill="#1c1c1d"/>
        <polygon points="286,0 540,0 540,26 282,26" fill="#3a4fa8"/>
      </svg>
    </section>
  </main>
</body>
</html>
```